Tour operator needs simple coded WordPress site (updated extra payment for coding and guaranteed)

[update 9/7/2015]
If you design a new logo and it gets accepted, even if we use another template with your logo you will get $50
[update 8/7/2015]
Update on questions about dual-language
For dual languages we are happy to set up a second site with the same designs in a second language.
For the design aspect just allow the user to switch between languages with an icon.
For the coding, a replica of the site on a second server will do (to save messing around with multiple language plugins) - we will populate it with Chinese text
[original post]
Simple coded WordPress site for tours
You can choose to design only or design and code ($340 design, $150 bonus for coding)
Open design brief - use your creativity
Will be in 2 languages (English and Chinese) but design needs only to be in one language
Winning design will be chosen only from home page, but the winner must make a second standard template page when chosen at no extra cost.
Must be responsive design
We only need homepage and standard template page design and coding, we will populate the pages
You can use design ideas from our pamphlet if you like - attached
Only a sample logo and colors on website and pamphlet - feel free to change as the current ones seem restrictive
Current website framework only to give an idea of the number of pages and basic menu structure (no need to use existing navigation style or any style at all for that matter, open brief)
http://brightwaterlearningtrips.com.au/
Target Market(s)
Chinese parents of kids 10-14 (the kids will take the tour)
Industry/Entity Type
Tour
Number of Pages Required
2 page
Look and feel
Each slider illustrates characteristics of the customer's brand and the style your logo design should communicate.

```html
<!DOCTYPE html>
<html lang="en">
<head>
<meta charset="utf-8">
<title>Brightwater Learning Trips</title>
<link href="https://fonts.googleapis.com/css2?family=Lato:wght@400;700&family=Oswald:wght@400;500&display=swap" rel="stylesheet">
<style>
:root{
  --navy:#2f3b82;
  --gold:#f2af1c;
  --ink:#333;
  --body:#5a5a5a;
  --rule:#d6d6d6;
  --panel:#ececec;
  --footer:#1b1b1b;
}
*{box-sizing:border-box;margin:0;padding:0}
html,body{width:926px;height:1200px;overflow:hidden}
body{font-family:'Lato',sans-serif;color:var(--body);background:#fff;position:relative}
.hero{position:absolute;left:0;top:0;width:926px;height:476px;
  background:linear-gradient(180deg,#2b3140 0%,#5a4a38 30%,#9a6a30 52%,#6b4a2c 72%,#2a2420 100%)}
.lang{position:absolute;left:748px;top:15px;width:78px;height:24px;border:2px solid #fff;color:#fff;
  font:700 12px 'Lato',sans-serif;display:flex;align-items:center;justify-content:space-between;padding:0 8px 0 9px}
.slide-arrow{position:absolute;top:199px}
.logo-box{position:absolute;left:101px;top:304px;width:216px;height:109px;background:#fff;
  display:flex;align-items:center;justify-content:center;gap:8px}
.logo-box .dot{width:22px;height:22px;border-radius:50%;background:var(--gold)}
.logo-box .name{font:700 15px/1.2 'Lato',sans-serif;color:var(--navy);text-transform:uppercase;width:130px}
.tagline{position:absolute;right:102px;top:362px;text-align:right;color:#fff;
  font:400 22px/28px 'Oswald',sans-serif;text-transform:uppercase;letter-spacing:-.2px}
.nav{position:absolute;left:0;top:429px;width:926px;height:47px;border-top:1px solid rgba(255,255,255,.35)}
.nav a{position:absolute;top:0;height:47px;line-height:47px;color:#fff;font:700 12px/47px 'Lato',sans-serif;text-decoration:none;text-align:center;width:112px}
.nav a.active{background:#fff;color:var(--navy)}
.social{position:absolute;top:437px;width:30px;height:30px;border:2px solid #fff;border-radius:50%}

.welcome{position:absolute;left:101px;top:506px;width:456px}
.welcome h1{font:400 24px/30px 'Oswald',sans-serif;color:var(--ink);text-transform:uppercase;padding-bottom:4px;border-bottom:1px solid var(--rule);letter-spacing:-.3px}
.welcome h1 .n{color:var(--navy)} .welcome h1 .g{color:var(--gold)}
.lead{font:700 12px/16px 'Lato',sans-serif;color:#555;margin:8px 0 6px 1px}
.welcome p.copy{font-size:10px;line-height:13.5px;margin:0 0 5px 1px}
.btn{display:inline-block;background:var(--navy);color:#fff;font:700 13px/26px 'Lato',sans-serif;text-transform:uppercase;text-align:center;border:0}
.welcome .btn{position:absolute;left:351px;top:184px;width:105px}
.divider{position:absolute;left:575px;top:506px;width:1px;height:210px;background:var(--rule)}
.inquiry{position:absolute;left:598px;top:506px;width:227px}
.inquiry h2{font:400 24px/30px 'Oswald',sans-serif;color:var(--ink);text-transform:uppercase;letter-spacing:-.3px}
.field{display:block;width:227px;height:26px;border:1px solid #ccc;margin-top:7px;font:400 11px/24px 'Lato',sans-serif;color:#999;padding-left:7px}
.field:first-of-type{margin-top:15px}
.field.msg{height:58px}
.inquiry .btn{position:absolute;left:122px;top:184px;width:105px}

.features{position:absolute;left:0;top:733px;width:926px;height:380px;background:var(--panel)}
.card{position:absolute;top:38px;width:347px;height:305px;background:#fff;border:1px solid #ddd;border-top:3px solid var(--gold);padding:14px 14px 0 13px}
.card h3{display:flex;align-items:flex-end;gap:8px;font:400 18px/22px 'Oswald',sans-serif;color:var(--navy);text-transform:uppercase;letter-spacing:-.3px}
.card h3 span{flex:1;border-bottom:1px dotted #aaa;padding-bottom:2px}
.card ul{list-style:none;margin-top:9px}
.card li{position:relative;padding-left:24px;font-size:10px;line-height:13px;margin-bottom:8px}
.card.safe li{margin-bottom:5.5px}
.card li svg{position:absolute;left:0;top:0}

.newsletter{position:absolute;left:0;top:1113px;width:926px;height:44px;background:var(--navy);color:#fff}
.newsletter .env{position:absolute;left:101px;top:5px}
.newsletter .title{position:absolute;left:145px;top:9px;font:400 19px/24px 'Lato',sans-serif}
.newsletter .chev{position:absolute;left:344px;top:5px}
.newsletter .sub{position:absolute;left:390px;top:15px;font-size:11.5px}
.newsletter .email{position:absolute;left:571px;top:11px;width:189px;height:22px;background:#fff;color:#333;font-size:10px;line-height:22px;padding-left:7px}
.newsletter .go{position:absolute;left:767px;top:11px;width:58px;height:22px;background:#111;border:1px solid #fff;font:700 10px/20px 'Lato',sans-serif;text-align:center}
.footer{position:absolute;left:0;top:1157px;width:926px;height:43px;background:var(--footer);color:#fff;font-size:10px}
.footer .links{position:absolute;left:102px;top:14px}
.footer .copy{position:absolute;right:103px;top:14px}
</style>
</head>
<body>
<header class="hero" role="img" aria-label="Photo of a harbour city skyline with an opera house and arch bridge at sunset">
  <div class="lang">English
    <svg width="12" height="8" viewBox="0 0 12 8"><path d="M1 1l5 5 5-5" fill="none" stroke="#fff" stroke-width="1.6"/></svg>
  </div>
  <svg class="slide-arrow" style="left:62px" width="40" height="78" viewBox="0 0 40 78"><path d="M39 1L1 39l38 38" fill="none" stroke="#fff" stroke-width="1"/></svg>
  <svg class="slide-arrow" style="left:825px" width="40" height="78" viewBox="0 0 40 78"><path d="M1 1l38 38L1 77" fill="none" stroke="#fff" stroke-width="1"/></svg>
  <div class="logo-box"><span class="dot"></span><span class="name">Brightwater Learning Trips</span></div>
  <p class="tagline">Educational, safe, culturally Brightwater Learning<br>Trips enlightening and fun.</p>
  <nav class="nav">
    <a class="active" href="#" style="left:101px">Home</a>
    <a href="#" style="left:220px">About Us</a>
    <a href="#" style="left:339px">Tours</a>
    <a href="#" style="left:464px">Contact Us</a>
    <span class="social" style="left:714px" aria-label="Social link"></span>
    <span class="social" style="left:754px" aria-label="Social link"></span>
    <span class="social" style="left:794px" aria-label="Social link"></span>
  </nav>
</header>

<section class="welcome">
  <h1>Welcome to <span class="n">Brightwater</span> <span class="g">Learning</span> <span class="n">Trips</span></h1>
  <p class="lead">At Brightwater Learning Trips we are passionate about educational travel and opportunities for students to gain academic and cultural understanding of Australia.</p>
  <p class="copy">14 day premium cultural and educational tours to Australian cities. Educational, safe, culturally enlightening and fun. Learn about educational institutions, history, sports, laws and customs, food and culture while improving your English.</p>
  <p class="copy">At Brightwater Learning Trips we are passionate about educational travel and providing opportunities for students to learn more about a country and gain a deeper understanding of the culture. The out of classroom experience gained on our trips is invaluable.</p>
  <span class="btn">Read More</span>
</section>
<div class="divider"></div>
<section class="inquiry">
  <h2>Quick Inquiry</h2>
  <span class="field">Name</span>
  <span class="field">Email</span>
  <span class="field msg">Message</span>
  <span class="btn">Submit</span>
</section>

<section class="features">
  <article class="card" style="left:101px">
    <h3><svg width="30" height="20" viewBox="0 0 30 20"><path d="M15 2L1 8l14 6 14-6z" fill="#f2af1c"/><path d="M7 11v5c4 3 12 3 16 0v-5l-8 3z" fill="#f2af1c"/><path d="M27 9v7" stroke="#f2af1c" stroke-width="1.5"/></svg><span>Educational and Cultural</span></h3>
    <ul>
      <li><svg width="18" height="12" viewBox="0 0 18 12"><path d="M1 11C4 5 8 4 11 4V1l6 5-6 5V8C7 8 4 9 1 11z" fill="#2f3b82"/></svg>Professional lecturers from Sydney universities</li>
      <li><svg width="18" height="12" viewBox="0 0 18 12"><path d="M1 11C4 5 8 4 11 4V1l6 5-6 5V8C7 8 4 9 1 11z" fill="#2f3b82"/></svg>2 hour lessons every day in easy to understand,<br>high-quality English</li>
      <li><svg width="18" height="12" viewBox="0 0 18 12"><path d="M1 11C4 5 8 4 11 4V1l6 5-6 5V8C7 8 4 9 1 11z" fill="#2f3b82"/></svg>Subjects from the Australian Educational Curriculum as well as cultural information on Australia</li>
      <li><svg width="18" height="12" viewBox="0 0 18 12"><path d="M1 11C4 5 8 4 11 4V1l6 5-6 5V8C7 8 4 9 1 11z" fill="#2f3b82"/></svg>How to live, get around, shop and socialise in Australia</li>
      <li><svg width="18" height="12" viewBox="0 0 18 12"><path d="M1 11C4 5 8 4 11 4V1l6 5-6 5V8C7 8 4 9 1 11z" fill="#2f3b82"/></svg>Attitudes to languages, food, religion and culture</li>
      <li><svg width="18" height="12" viewBox="0 0 18 12"><path d="M1 11C4 5 8 4 11 4V1l6 5-6 5V8C7 8 4 9 1 11z" fill="#2f3b82"/></svg>Outdoor activities and sport</li>
    </ul>
  </article>
  <article class="card safe" style="left:478px">
    <h3><svg width="22" height="24" viewBox="0 0 22 24"><path d="M6 11V7a5 5 0 0110 0v4" fill="none" stroke="#f2af1c" stroke-width="2.5"/><rect x="3" y="11" width="16" height="12" rx="1" fill="#f2af1c"/><circle cx="11" cy="16" r="2" fill="#fff"/></svg><span>Safe and Secure</span></h3>
    <ul>
      <li><svg width="18" height="12" viewBox="0 0 18 12"><path d="M1 11C4 5 8 4 11 4V1l6 5-6 5V8C7 8 4 9 1 11z" fill="#2f3b82"/></svg>Staff certified by the government for Working With Children</li>
      <li><svg width="18" height="12" viewBox="0 0 18 12"><path d="M1 11C4 5 8 4 11 4V1l6 5-6 5V8C7 8 4 9 1 11z" fill="#2f3b82"/></svg>Staff certified in first aid care</li>
      <li><svg width="18" height="12" viewBox="0 0 18 12"><path d="M1 11C4 5 8 4 11 4V1l6 5-6 5V8C7 8 4 9 1 11z" fill="#2f3b82"/></svg>Professional accommodation with excellent history in caring for children with extremely well documented Safety Management Procedures including;</li>
      <li><svg width="18" height="12" viewBox="0 0 18 12"><path d="M1 11C4 5 8 4 11 4V1l6 5-6 5V8C7 8 4 9 1 11z" fill="#2f3b82"/></svg>Safety Management - reducing risk when taking students out of the classroom</li>
      <li><svg width="18" height="12" viewBox="0 0 18 12"><path d="M1 11C4 5 8 4 11 4V1l6 5-6 5V8C7 8 4 9 1 11z" fill="#2f3b82"/></svg>Safety &amp; Emergency Procedures (Location-specific)</li>
      <li><svg width="18" height="12" viewBox="0 0 18 12"><path d="M1 11C4 5 8 4 11 4V1l6 5-6 5V8C7 8 4 9 1 11z" fill="#2f3b82"/></svg>Standard Operating Procedures</li>
      <li><svg width="18" height="12" viewBox="0 0 18 12"><path d="M1 11C4 5 8 4 11 4V1l6 5-6 5V8C7 8 4 9 1 11z" fill="#2f3b82"/></svg>Activity-Specific Risk Management Matrix</li>
      <li><svg width="18" height="12" viewBox="0 0 18 12"><path d="M1 11C4 5 8 4 11 4V1l6 5-6 5V8C7 8 4 9 1 11z" fill="#2f3b82"/></svg>Area Assessment Documentation</li>
      <li><svg width="18" height="12" viewBox="0 0 18 12"><path d="M1 11C4 5 8 4 11 4V1l6 5-6 5V8C7 8 4 9 1 11z" fill="#2f3b82"/></svg>Medical Form, Dietary Requirements Form, First Aid Incident &amp; Management Forms</li>
      <li><svg width="18" height="12" viewBox="0 0 18 12"><path d="M1 11C4 5 8 4 11 4V1l6 5-6 5V8C7 8 4 9 1 11z" fill="#2f3b82"/></svg>Clothing &amp; Equipment List</li>
    </ul>
  </article>
</section>

<section class="newsletter">
  <svg class="env" width="34" height="34" viewBox="0 0 34 34"><circle cx="17" cy="17" r="15.5" fill="none" stroke="#fff" stroke-width="2"/><rect x="9" y="11" width="16" height="12" fill="#fff"/><path d="M9 11l8 7 8-7" fill="none" stroke="#2f3b82" stroke-width="1.5"/></svg>
  <span class="title">Newsletter Signup</span>
  <svg class="chev" width="28" height="34" viewBox="0 0 28 34"><path d="M2 1l14 16L2 33M10 1l14 16-14 16" fill="none" stroke="#fff" stroke-width="1.2"/></svg>
  <span class="sub">Signup For Free Email Updates</span>
  <span class="email">Enter your email here</span>
  <span class="go">SUBMIT</span>
</section>
<footer class="footer">
  <span class="links">Home &nbsp;|&nbsp; About Us &nbsp;|&nbsp; Tours &nbsp;|&nbsp; Contact Us</span>
  <span class="copy">© 2015 BRIGHTWATER LEARNING TRIPS. &nbsp;|&nbsp; All Rights Reserved.</span>
</footer>
</body>
</html>
```